Simple elegant business card

General card for a fin and television director.
Just want name, email, phone and address.

Target Market(s)

Prospective employers

Industry/Entity Type

Business

Requirements
Must have
• As above
Nice to have
• Logo but not necessary.
Should not have
• Not too colourful or funky.
• Simplicity and elegance the way to go.

```html
<!DOCTYPE html>
<html lang="en">
<head>
<meta charset="utf-8">
<title>Nora Vale – Business Card</title>
<link href="https://fonts.googleapis.com/css2?family=Arimo:wght@700&family=Tinos:ital,wght@0,400;1,400&display=swap" rel="stylesheet">
<style>
  :root {
    --page-bg: #e9e9ec;
    --card-white: #ffffff;
    --brand-red: #c3373b;
    --back-center: #ffffff;
    --back-mid: #f3e6e6;
    --back-edge: #d4a5a7;
    --rule-blue: #2f3f9a;
    --ink: #111111;
    --brand-purple: #5b2a86;
    --globe-light: #c4ceda;
    --globe-dark: #647a92;
    --card-edge: #222222;
  }
  * { box-sizing: border-box; margin: 0; padding: 0; }
  html, body {
    width: 1200px;
    height: 960px;
    overflow: hidden;
    background: var(--page-bg);
  }
  .canvas {
    position: relative;
    width: 1200px;
    height: 960px;
  }
  .card {
    position: absolute;
    left: 250px;
    width: 700px;
    height: 400px;
    overflow: hidden;
    box-shadow: 0 6px 18px rgba(0,0,0,0.18);
  }
  .card--front { top: 50px; background: var(--card-white); }
  .card--back {
    top: 500px;
    border: 3px solid var(--card-edge);
    background: radial-gradient(circle at 50% 42%, var(--back-center) 0%, var(--back-mid) 35%, var(--back-edge) 100%);
  }
  .front-band { position: absolute; inset: 0; }
  .wordmark {
    position: absolute;
    left: 0; right: 0;
    display: flex;
    flex-direction: column;
    align-items: center;
    font-family: "Tinos", "Times New Roman", serif;
    color: var(--brand-purple);
    letter-spacing: 1px;
  }
  .wordmark--small { top: 16px; font-size: 26px; gap: 4px; color: #ffffff; }
  .wordmark--small .mark-dot {
    width: 52px; height: 52px; border-radius: 50%;
    background: radial-gradient(circle at 40% 35%, var(--globe-light), var(--globe-dark));
    border: 2px solid #ffffff;
  }
  .identity {
    position: absolute;
    left: 38px;
    top: 226px;
  }
  .identity__name {
    font-family: "Arimo", Arial, sans-serif;
    font-weight: 700;
    font-size: 30px;
    color: var(--ink);
  }
  .identity__role {
    font-family: "Tinos", "Times New Roman", serif;
    font-style: italic;
    font-size: 22px;
    color: var(--ink);
    margin-left: 30px;
  }
  .contact {
    position: absolute;
    left: 276px;
    top: 196px;
    font-family: "Tinos", "Times New Roman", serif;
    font-size: 24px;
    line-height: 34px;
    color: var(--ink);
  }
  .contact__label { display: inline-block; width: 96px; }
  .wordmark--large { top: 60px; font-size: 38px; gap: 22px; }
  .wordmark--large .mark-dot {
    width: 210px; height: 210px; border-radius: 50%;
    background: radial-gradient(circle at 38% 32%, var(--globe-light), var(--globe-dark));
  }
</style>
</head>
<body>
<main class="canvas">
  <section class="card card--front" aria-label="Business card front">
    <svg class="front-band" width="700" height="400" viewBox="0 0 700 400" aria-hidden="true">
      <path d="M0 0 H700 V95 C560 150 360 70 0 175 Z" fill="var(--brand-red)"/>
      <path d="M0 175 C360 70 560 150 700 95" fill="none" stroke="var(--rule-blue)" stroke-width="3"/>
    </svg>
    <div class="wordmark wordmark--small">
      <span class="mark-dot" role="img" aria-label="Round emblem"></span>
      <span class="mark-name">NORA VALE</span>
    </div>
    <div class="identity">
      <p class="identity__name">Nora Vale</p>
      <p class="identity__role">Tv Director</p>
    </div>
    <div class="contact">
      <p><span class="contact__label">Email:</span>noravale@studiomail.net</p>
      <p><span class="contact__label">Phone:</span>+1 555 014 2287</p>
      <p><span class="contact__label">Address:</span>48 Linden Row, Ojai CA</p>
    </div>
  </section>

  <section class="card card--back" aria-label="Business card back">
    <div class="wordmark wordmark--large">
      <span class="mark-dot" role="img" aria-label="Globe emblem"></span>
      <span class="mark-name">NORA VALE</span>
    </div>
  </section>
</main>
</body>
</html>
```